Re-Design Korbalex.com make it more professional looking

We want to re-design this website, we are currently not happy with existing design. Some of the design examples are listed below.

https://trelvan.com/
https://www.quostel.com/
https://www.namity.com/projects/
https://www.flarnside.com/

The content on the website is final, there will be no change in the content. We just need to re-design the site. Features page on the site is very important and need to be layout very well.

Industry/Entity Type

It Professional

Number of Pages Required

4 page

Font styles to use
Sans Serif

Requirements
Must have
• Professional look and design like the examples i quoted above and a nice color theme. I do not have preferences but i like the quostel.com and trelvan.com

```html
<!DOCTYPE html>
<html lang="en">
<head>
<meta charset="utf-8">
<title>Korbalex – Organize, Collaborate and Deliver</title>
<link href="https://fonts.googleapis.com/css2?family=Arimo:wght@400;700&family=Open+Sans:wght@400;600;700&display=swap" rel="stylesheet">
<style>
:root{
  --header-bg:#ececec;
  --ink:#3d3d3d;
  --logo-grey:#6a6a6a;
  --orange:#f5ad26;
  --dark:#333232;
  --footer:#383737;
  --footer-bottom:#4b4a4a;
  --white:#ffffff;
  --blue-1:#2b6f92;
  --blue-2:#123f58;
  --wall-light:#d6d6d3;
  --wall-mid:#aeaeab;
  --wall-dark:#7e7e7b;
  --shirt:#f4f4f2;
  --skin:#c9a58c;
  --suit-dark:#2a2a2c;
}
*{margin:0;padding:0;box-sizing:border-box}
html,body{width:1200px;height:3416px;overflow:hidden}
body{position:relative;font-family:"Arimo",Arial,sans-serif;color:var(--ink);background:var(--dark)}
.abs{position:absolute}

/* header */
.site-header{position:absolute;left:0;top:0;width:1200px;height:155px;background:var(--header-bg)}
.brand{position:absolute;left:60px;top:82px;display:flex;align-items:center;gap:12px}
.brand-dot{width:34px;height:34px;border-radius:50%;background:var(--orange)}
.brand-name{font-family:"Open Sans",sans-serif;font-weight:700;font-size:50px;color:var(--logo-grey);letter-spacing:-1px;line-height:1}
.main-nav{position:absolute;right:68px;top:114px;display:flex;align-items:center;gap:7px;font-family:"Open Sans",sans-serif;font-weight:700;font-size:10px;color:#222}
.main-nav .btn-outline{border:1.5px solid #222;padding:6px 6px;line-height:1}

/* hero */
.hero{position:absolute;left:0;top:155px;width:1200px;height:792px;
  background:
    radial-gradient(ellipse 260px 360px at 860px 640px,var(--shirt) 0%,rgba(244,244,242,.7) 45%,rgba(244,244,242,0) 100%),
    radial-gradient(ellipse 70px 260px at 1010px 650px,var(--suit-dark) 0%,rgba(42,42,44,0) 100%),
    radial-gradient(ellipse 150px 170px at 960px 300px,var(--skin) 0%,rgba(201,165,140,0) 100%),
    radial-gradient(ellipse 160px 130px at 1010px 170px,#5a4536 0%,rgba(90,69,54,0) 100%),
    radial-gradient(ellipse 520px 420px at 420px 320px,var(--wall-light) 0%,rgba(214,214,211,0) 100%),
    linear-gradient(180deg,var(--wall-mid) 0%,#a2a29f 60%,var(--wall-dark) 100%)}
.hero-title{position:absolute;left:105px;top:540px;width:340px;text-align:right;font-family:"Arimo",sans-serif;font-weight:400;font-size:57px;line-height:66px;color:var(--white);text-shadow:0 2px 6px rgba(0,0,0,.35)}

/* intro */
.intro{position:absolute;left:0;top:947px;width:1200px;height:313px;background:var(--dark)}
.video-thumb{position:absolute;left:68px;top:55px;width:337px;height:187px;background:linear-gradient(135deg,#5a5a5a,#444)}
.intro-text{position:absolute;left:428px;top:54px;width:244px;font-size:13.5px;line-height:19.5px;color:#8f8f8f;text-align:justify}
.intro-cta{position:absolute;left:1029px;top:62px;width:114px;height:68px;border:1.5px solid var(--orange);color:var(--orange);font-size:9px;line-height:11px;padding:20px 0 0 10px}
.intro-cta svg{position:absolute;right:10px;top:8px}

/* mission slider */
.mission{position:absolute;left:0;top:1260px;width:1200px;height:657px;background:linear-gradient(160deg,var(--blue-1) 0%,#1e5878 45%,var(--blue-2) 100%)}
.mission-text{position:absolute;left:205px;top:200px;width:795px;font-size:20.5px;line-height:30px;color:var(--white);text-align:justify}
.mission-text p+p{margin-top:30px}
.slider-dots{position:absolute;display:flex;gap:14px}
.slider-dots i{width:10px;height:10px;border-radius:50%;background:var(--white);display:block}
.slider-dots i.on{background:var(--orange)}

/* integrations */
.integrations{position:absolute;left:0;top:1917px;width:1200px;height:661px;background:var(--dark)}
.integrations h2{position:absolute;left:0;width:1200px;top:150px;text-align:center;font-weight:400;font-size:26px;color:var(--orange)}
.app-list{position:absolute;left:210px;top:228px;display:flex;gap:12px;list-style:none}
.app-list li{width:121px;height:121px;border-radius:50%;background:var(--white);border:6px solid var(--orange);display:flex;align-items:center;justify-content:center;font-weight:700;font-size:16px;color:#555}
.feature-pitch{position:absolute;left:210px;top:390px;font-size:43px;color:var(--orange);white-space:nowrap}
.feature-sub{position:absolute;left:210px;top:460px;width:440px;font-size:13px;line-height:16px;color:#ddd}
.view-features{position:absolute;left:888px;top:451px;width:100px;height:38px;border:1.5px solid var(--orange);color:var(--orange);font-size:11px;line-height:12px;padding:7px 0 0 14px}
.view-features svg{position:absolute;right:10px;top:11px}

/* testimonial */
.testimonial{position:absolute;left:0;top:2578px;width:1200px;height:373px;background:linear-gradient(180deg,#5e6066 0%,#44464b 60%,#2f3034 100%)}
.avatar{position:absolute;left:203px;top:38px;width:143px;height:143px;border-radius:50%;background:#e8e8e8;border:4px solid var(--white)}
.quote{position:absolute;left:369px;top:96px;width:630px;font-size:13px;line-height:15.5px;color:#eee}
.quote-author{position:absolute;left:369px;top:238px;font-size:14px;line-height:17px;color:var(--white)}
.quote-author b{display:block;color:var(--orange);font-weight:700}

/* offer band */
.offer{position:absolute;left:0;top:2951px;width:1200px;height:100px;background:var(--orange)}
.offer p{position:absolute;left:0;top:22px;width:1200px;text-align:center;font-size:26px;color:#2a2a2a}
.offer a{position:absolute;right:130px;top:72px;font-size:14px;color:#2a2a2a;text-decoration:none;letter-spacing:.3px}

/* footer */
.site-footer{position:absolute;left:0;top:3051px;width:1200px;height:296px;background:var(--footer)}
.footer-col{position:absolute;top:54px;list-style:none;font-size:10px;line-height:15px;color:#bdbdbd}
.footer-col h3{font-size:10px;font-weight:700;color:var(--orange);margin-bottom:3px}
.help{position:absolute;left:797px;top:50px;font-size:11px;color:var(--orange)}
.phone{position:absolute;left:920px;top:46px;font-size:32px;color:var(--orange)}
.email{position:absolute;left:920px;top:95px;font-size:20px;color:#8a8a8a}
.footer-bottom{position:absolute;left:0;top:3347px;width:1200px;height:69px;background:var(--footer-bottom);font-size:10px;color:#aaa;padding:32px 0 0 41px}
</style>
</head>
<body>

<header class="site-header">
  <div class="brand"><span class="brand-dot"></span><span class="brand-name">Korbalex</span></div>
  <nav class="main-nav">
    <span>HOME</span><span>FEATURES</span><span>PRICING</span><span>ABOUT US</span><span>CONTACT US</span>
    <span class="btn-outline">LOGIN</span><span class="btn-outline">GET STARTED NOW</span>
  </nav>
</header>

<section class="hero" role="img" aria-label="Photo of a young man in glasses, white shirt and dark tie sketching a light bulb on a grey wall covered with small bulb drawings">
  <h1 class="hero-title">Organize,<br>Collaborate<br>and Deliver</h1>
</section>

<section class="intro">
  <div class="video-thumb" role="img" aria-label="Video preview of a person working at a desk">
    <svg width="337" height="187" viewBox="0 0 337 187"><circle cx="168" cy="93" r="40" fill="none" stroke="#bbb" stroke-width="4"/><path d="M155 72 L188 93 L155 114 Z" fill="none" stroke="#bbb" stroke-width="4"/></svg>
  </div>
  <p class="intro-text">Being an SEO agency we did not find any tool that can help agencies to manage an SEO project lifecycle effectively. That is why we decided to bring Korbalex "A robust SEO project management tool" for SEO Agencies to provide them the solution to manage their projects in an organized way.</p>
  <div class="intro-cta">Features<br>for Digital<br>Agencies
    <svg width="12" height="14" viewBox="0 0 12 14"><path d="M1 1 L11 7 L1 13 Z" fill="none" stroke="#f5ad26" stroke-width="1.5"/></svg>
  </div>
</section>

<section class="mission" aria-label="Why Korbalex">
  <svg class="abs" style="left:40px;top:250px" width="50" height="140" viewBox="0 0 50 140"><path d="M46 2 L4 70 L46 138" fill="none" stroke="#f5ad26" stroke-width="3"/></svg>
  <svg class="abs" style="left:1112px;top:250px" width="50" height="140" viewBox="0 0 50 140"><path d="M4 2 L46 70 L4 138" fill="none" stroke="#f5ad26" stroke-width="3"/></svg>
  <div class="mission-text">
    <p>Now SEO management is not at all a hectic task. Organize your SEO projects more effectively &amp; efficiently. Korbalex helps you to track every pitfall to projects and to find out their solutions on time. Give a powerful tool to your team to schedule their priorities &amp; finish things on time. Korbalex guides you to do the right things than to do things right. It's the most effective online tool that makes tasks easy and extremely manageable.</p>
    <p>Make your projects more interesting and their solutions so constructive!</p>
  </div>
  <div class="slider-dots" style="left:576px;top:609px"><i class="on"></i><i class="on"></i><i></i></div>
</section>

<section class="integrations">
  <svg class="abs" style="left:40px;top:262px" width="46" height="134" viewBox="0 0 46 134"><path d="M44 2 L4 67 L44 132" fill="none" stroke="#8a8a8a" stroke-width="2"/></svg>
  <svg class="abs" style="left:1112px;top:262px" width="46" height="134" viewBox="0 0 46 134"><path d="M2 2 L42 67 L2 132" fill="none" stroke="#8a8a8a" stroke-width="2"/></svg>
  <h2>Integrated with some of the most popular apps you already love.</h2>
  <ul class="app-list">
    <li>Dravel</li><li>Metricon</li><li>Boxwell</li><li>Ledgerly</li><li>Socialo</li><li>Skyvault</li>
  </ul>
  <p class="feature-pitch">See what makes Korbalex a perfect tool!</p>
  <p class="feature-sub">See yourself the features that make Korbalex a perfect tool to manage your projects and get things done efficiently and in time.</p>
  <div class="view-features">View<br>Features
    <svg width="12" height="14" viewBox="0 0 12 14"><path d="M1 1 L11 7 L1 13 Z" fill="none" stroke="#f5ad26" stroke-width="1.5"/></svg>
  </div>
  <div class="slider-dots" style="left:576px;top:605px"><i class="on"></i><i></i><i></i></div>
</section>

<section class="testimonial" role="img" aria-label="Background photo of city buildings and a bare tree at dusk">
  <svg class="abs" style="left:40px;top:95px" width="46" height="134" viewBox="0 0 46 134"><path d="M44 2 L4 67 L44 132" fill="none" stroke="#bbb" stroke-width="2"/></svg>
  <svg class="abs" style="left:1112px;top:95px" width="46" height="134" viewBox="0 0 46 134"><path d="M2 2 L42 67 L2 132" fill="none" stroke="#bbb" stroke-width="2"/></svg>
  <div class="avatar" role="img" aria-label="Portrait of the reviewer"></div>
  <p class="quote">" We have been struggling to meet our goals as well as client's objective. It was at this point, we came across SEO project management tool. Korbalex automated SEO Project Management Tool has certainly added value to our core process. It has empowered every aspect of SEO campaign. With the tool we are effectively able to allocate tasks, keep a track of all our projects and campaigns. It has covered up every minute detail and simplified the complex process of project management. The results are fantastic. Kudos Korbalex for coming up with a practical SEO project management tool. "</p>
  <p class="quote-author"><b>Arlen Voss</b>Freelancer</p>
</section>

<section class="offer">
  <p>“Share your experience with us and get&nbsp; 3 months of premium access for free”.</p>
  <a href="#">START MY 30 DAYS FREE TRIAL</a>
</section>

<footer class="site-footer">
  <ul class="footer-col" style="left:91px">
    <h3>MENU</h3>
    <li>Home</li><li>Features</li><li>Pricing</li><li>About Us</li><li>Contact Us</li>
  </ul>
  <ul class="footer-col" style="left:233px">
    <h3>FEATURES</h3>
    <li>Project Management</li><li>Constructive Dashboard</li><li>User level Interface</li><li>Password Manager</li><li>Link Manager</li><li>Client Management</li><li>Customize brand</li><li>Billing Management</li><li>Milestone Management</li><li>Event Management</li><li>File manager</li><li>Task management</li>
  </ul>
  <ul class="footer-col" style="left:440px">
    <h3>RESOURCES</h3>
    <li>Testimonials</li><li>3rd Party Apps</li><li>Newsletter</li><li>Support &amp; FAQs</li><li>Privacy Policy</li><li>Refund Policy</li>
  </ul>
  <p class="help">HELP &amp; SUPPORT</p>
  <p class="phone">+1-555-010-4420</p>
  <p class="email">help@korbalex.com</p>
</footer>
<div class="footer-bottom">© 2016, Korbalex by Korbalex Labs Pvt Ltd. All Rights Reserved.</div>

</body>
</html>
```